I am a new company with the latest technology in the concrete polishing business

We need a logo design for a new company out of Toronto, Canada. We polish residential, commercial and industrial concrete as well as different epoxy toppings.

Target Market(s)

How Owners with expendable incomes

Industry/Entity Type

Construction

Contact Information for Business Card

be able to see content rather easily

Colors
0355a3
fbed22
1b1b1b

Requirements
Must have
• simple and elegant

```html
<!DOCTYPE html>
<html lang="en">
<head>
<meta charset="utf-8">
<title>Slabline Coatings – Business Card</title>
<link href="https://fonts.googleapis.com/css2?family=Source+Sans+3:wght@400;600;700&display=swap" rel="stylesheet">
<style>
  :root {
    --brand-blue: #0355a3;
    --brand-yellow: #fbed22;
    --ink: #1b1b1b;
    --paper: #ffffff;
    --backdrop: #555555;
    --rule: #7a7fa8;
  }
  * { margin: 0; padding: 0; box-sizing: border-box; }
  html, body {
    width: 1200px; height: 900px; overflow: hidden;
    background: var(--backdrop);
    font-family: "Source Sans 3", "Segoe UI", sans-serif;
    color: var(--ink);
  }
  .canvas { position: relative; width: 1200px; height: 900px; }

  .card {
    position: absolute; top: 170px;
    width: 347px; height: 560px;
    overflow: hidden;
  }

  /* Front */
  .card--front { left: 259px; background: var(--paper); text-align: center; }
  .brand-square {
    position: absolute; left: 129px; top: 105px;
    width: 90px; height: 85px;
    background: var(--brand-blue);
  }
  .brand-name {
    position: absolute; left: 0; right: 0; top: 208px;
    font-size: 30px; font-weight: 700; letter-spacing: -0.3px;
    color: var(--brand-blue);
  }
  .contact-block { position: absolute; left: 0; right: 0; top: 339px; }
  .person-name { font-size: 21px; font-weight: 600; line-height: 26px; }
  .person-name .first { color: var(--brand-blue); }
  .person-name .last { color: var(--brand-yellow); }
  .person-title { font-size: 15px; line-height: 20px; }
  .divider {
    width: 130px; height: 1px; margin: 10px auto 10px;
    background: var(--rule);
  }
  .contact-line { font-size: 15px; line-height: 21px; }
  .contact-line .label { color: var(--brand-blue); font-weight: 600; }
  .contact-line--web { color: var(--brand-blue); font-weight: 600; }
  .contact-line--web .domain { color: var(--brand-yellow); }
  .address-line { font-size: 15px; line-height: 18px; }

  /* Back */
  .card--back { left: 631px; background: var(--brand-yellow); }
  .band-blue {
    position: absolute; left: 0; top: 0;
    width: 173px; height: 100%;
    background: var(--brand-blue);
  }
  .back-name {
    position: absolute; left: 0; right: 0; top: 262px;
    text-align: center;
    font-size: 32px; font-weight: 700;
    color: var(--paper);
  }
  .back-web {
    position: absolute; left: 0; right: 0; top: 485px;
    text-align: center;
    font-size: 19px; font-weight: 700;
    color: var(--ink);
  }
</style>
</head>
<body>
<main class="canvas">
  <section class="card card--front">
    <div class="brand-square"></div>
    <div class="brand-name">Slabline Coatings</div>
    <div class="contact-block">
      <div class="person-name"><span class="first">DANIEL</span> <span class="last">REYES</span></div>
      <div class="person-title">Managing Director</div>
      <div class="divider"></div>
      <div class="contact-line"><span class="label">P:</span> 416-555-0182</div>
      <div class="contact-line"><span class="label">E:</span> hello@slablinecoatings.com</div>
      <div class="contact-line contact-line--web">www.<span class="domain">slablinecoatings</span>.com</div>
      <div class="divider"></div>
      <div class="address-line">88 Harbour Yard Road</div>
      <div class="address-line">Toronto, ON M5V 2K1</div>
    </div>
  </section>

  <section class="card card--back">
    <div class="band-blue"></div>
    <div class="back-name">Slabline Coatings</div>
    <div class="back-web">www.slablinecoatings.com</div>
  </section>
</main>
</body>
</html>
```